Pool Services Flyer promote regular pool services

We need a flyer design to be send out as a DL Postcard

We are a pool and spa maintenance business and would like to promote of regular pool services.
Please see our website www.brightripplepoolcare.com.au and our facebook page https://www.facebook.com/pages/Bright-Ripple-Pool-Care/583920174630518

We are pretty flexible with layouts etc Our monthly pool service is $67.00 plus chemicals so we would like this highlighted on our ad. We also so one off, weekly and fortnightly services as well.

We would like our details and logo on front and website also listed.

Target Market(s)

Pool owners

Industry/Entity Type

Pool Service

Colors
33a6d7
0292cd
0555a3
3276b5
85abd2

Requirements
Must have
• Logo
• website address
• phone number
• Price
• Promote the fact that customer wont have to worry about their pool
Nice to have
• like to have a blue wave down the bottom of flyer witht eh contact information in it. Would like to to be crisp not over crowed with information

```html
<!DOCTYPE html>
<html lang="en">
<head>
<meta charset="utf-8">
<title>Bright Ripple Pool Care – DL Postcard</title>
<link rel="stylesheet" href="https://fonts.googleapis.com/css2?family=Anton&family=Open+Sans:wght@400;600&display=swap">
<style>
  :root {
    --page-bg: #2b2d30;
    --navy: #0d2a45;
    --deep-blue: #0555a3;
    --mid-blue: #3276b5;
    --bright-blue: #0292cd;
    --sky-blue: #33a6d7;
    --pale-blue: #85abd2;
    --yellow: #ffe81a;
    --white: #ffffff;
    --logo-grey: #2e3338;
  }
  * { box-sizing: border-box; margin: 0; padding: 0; }
  html, body { width: 1200px; height: 1000px; overflow: hidden; }
  body { background: var(--page-bg); position: relative; font-family: "Open Sans", sans-serif; }

  .postcard {
    position: absolute; left: 60px; top: 242px;
    width: 1080px; height: 515px; overflow: hidden;
    background: var(--white);
  }
  .scene-photo {
    position: absolute; inset: 0;
    background:
      radial-gradient(ellipse 420px 180px at 640px 110px, rgba(255,255,255,.95), rgba(255,255,255,0) 70%),
      linear-gradient(180deg, #3f8fd0 0%, #8fc3ea 28%, #dff0fb 52%, #5fb2e2 60%, #2e9ad6 72%, #6fd0f0 100%);
  }
  .side-panel { position: absolute; left: 0; top: 0; width: 420px; height: 515px; }
  .photo-circle { position: absolute; border-radius: 50%; border: 5px solid var(--pale-blue); }
  .photo-family {
    left: -10px; top: -120px; width: 340px; height: 340px;
    background: linear-gradient(180deg, #2c8fd3 0%, #7cc6ee 55%, #f2d04a 85%, #e9b84a 100%);
  }
  .photo-massage {
    left: 15px; top: 165px; width: 185px; height: 185px;
    background: radial-gradient(circle at 60% 45%, #f4e4d8, #e7cdb9 55%, #f7f7f7 100%);
  }
  .splash-art {
    position: absolute; left: 0; top: 360px; width: 330px; height: 103px;
    background: linear-gradient(180deg, rgba(133,171,210,0) 0%, #5fb2e2 35%, #3276b5 70%, #0555a3 100%);
  }

  .brand {
    position: absolute; left: 525px; top: 50px;
    display: flex; align-items: center; gap: 14px;
  }
  .brand-dot { width: 58px; height: 58px; border-radius: 50%; background: var(--sky-blue); }
  .brand-name { font-family: "Open Sans", sans-serif; font-weight: 400; font-size: 30px; color: var(--logo-grey); }

  .headline {
    position: absolute; left: 293px; top: 170px;
    font-family: "Anton", sans-serif; font-size: 58px; line-height: 1; letter-spacing: 5.5px;
    color: var(--navy); white-space: nowrap;
    -webkit-text-stroke: 8px var(--white); paint-order: stroke fill;
    text-shadow: 3px 4px 4px rgba(0,0,0,.35);
  }
  .service-band {
    position: absolute; left: 480px; top: 247px; width: 567px; height: 32px;
    background: linear-gradient(90deg, rgba(255,255,255,.95), rgba(255,255,255,.75));
    font-family: "Anton", sans-serif; font-size: 23px; line-height: 32px; letter-spacing: 2px;
    color: var(--deep-blue); padding-left: 10px; white-space: nowrap;
  }
  .offer-label, .price, .price-note {
    position: absolute; font-family: "Anton", sans-serif; color: var(--yellow); white-space: nowrap;
    -webkit-text-stroke: 6px var(--navy); paint-order: stroke fill;
  }
  .offer-label { left: 213px; top: 262px; font-size: 50px; line-height: 52px; letter-spacing: 2.5px; text-align: center; }
  .price { left: 428px; top: 282px; font-size: 98px; line-height: 1; }
  .price .currency { font-size: 46px; vertical-align: 34px; margin-right: 4px; }
  .price .cents { font-size: 42px; vertical-align: 44px; }
  .price-note { left: 428px; top: 374px; font-size: 28px; line-height: 1; letter-spacing: 1px; }

  .contact-bar {
    position: absolute; left: 0; bottom: 0; width: 100%; height: 52px;
    background: var(--navy); border-top: 3px solid var(--white);
    font-family: "Anton", sans-serif; color: var(--white); font-size: 30px; letter-spacing: 1px;
  }
  .contact-phone { position: absolute; left: 232px; top: 4px; display: flex; align-items: center; gap: 16px; letter-spacing: 2px; }
  .contact-web { position: absolute; right: 28px; top: 4px; }
</style>
</head>
<body>
  <main class="postcard">
    <div class="scene-photo" role="img" aria-label="Sunny sky with clouds over the ocean and an infinity pool with a chrome ladder"></div>

    <svg class="side-panel" viewBox="0 0 420 515" aria-hidden="true">
      <path d="M0 0 H330 C330 140 300 200 250 240 C215 270 205 320 200 360 C195 400 180 440 150 470 L0 470 Z" fill="#3276b5"/>
      <path d="M0 0 H310 C310 130 285 190 238 228 C200 258 190 310 184 350 C178 395 165 430 140 460 L0 460 Z" fill="#33a6d7" opacity=".55"/>
    </svg>

    <div class="photo-circle photo-family" role="img" aria-label="Family of four on a yellow pool float"></div>
    <div class="photo-circle photo-massage" role="img" aria-label="Woman relaxing with a spa massage"></div>
    <div class="splash-art" role="img" aria-label="Water splash and blue wave illustration"></div>

    <div class="brand">
      <span class="brand-dot"></span>
      <span class="brand-name">Bright Ripple Pool Care</span>
    </div>

    <h1 class="headline">POOL N’ SPA MAINTENANCE</h1>
    <p class="service-band">FOR A ONE OFF, WEEKLY AND FORTNIGHTLY SERVICES</p>

    <p class="offer-label">MONTHLY<br>SERVICES</p>
    <p class="price"><span class="currency">$</span>67<span class="cents">.00</span></p>
    <p class="price-note">PLUS CHEMICALS</p>

    <footer class="contact-bar">
      <div class="contact-phone">
        <svg width="44" height="40" viewBox="0 0 44 40" aria-hidden="true">
          <path d="M4 14 C4 6 40 6 40 14 L34 18 C32 16 28 14 22 14 C16 14 12 16 10 18 Z" fill="#fff"/>
          <path d="M12 18 H32 L38 36 H6 Z" fill="#fff"/>
          <circle cx="22" cy="27" r="5" fill="#0d2a45"/>
        </svg>
        <span>(02) 4815 2937</span>
      </div>
      <div class="contact-web">WWW.BRIGHTRIPPLEPOOLCARE.COM.AU</div>
    </footer>
  </main>
</body>
</html>
```